Webpage for a treatment housing for young addicts.

I need a new design and files for my wordpress page. I need it to be more neat and clean. I need it to look professional with a starting page that will work as a navigation. I need like logo and phone number and such up top, a picture under it with one sentence as a slogan and under it 6 boxes to click to come to our different pages. Under it I want news etc.

Target Market(s)

Social services, employees and governements

Coding

Coded - Design and coding required

Font styles to use
Sans Serif

Colors
abd037
3176b5
9d9d9d
aaaaaa
f04a50

Requirements
Must have
• A nice design
Nice to have
• need it to look professional with a starting page that will work as a navigation. I need like logo and phone number and such up top, a picture under it with one sentence as a slogan and under it 6 boxes to click to come to our different pages. Under it I want news etc.
• today www.kelmora.se
• want more like www.trivest.se or www.solbrink.se
Should not have
• To many different colours and a messy design.

```html
<!DOCTYPE html>
<html lang="sv">
<head>
<meta charset="utf-8">
<title>Kelmora – Omsorg Vård Boende</title>
<link href="https://fonts.googleapis.com/css2?family=Poppins:wght@400;500;600&family=Oswald:wght@400;500&display=swap" rel="stylesheet">
<style>
:root{
  --blue:#3176b5;
  --green:#abd037;
  --red:#f04a50;
  --grey:#9d9d9d;
  --grey-light:#aaaaaa;
  --panel:#f2f2f2;
  --field:#e9e9e9;
  --ink:#333333;
  --muted:#666666;
  --white:#ffffff;
}
*{margin:0;padding:0;box-sizing:border-box}
html,body{width:1200px;height:2719px;overflow:hidden;background:var(--white)}
body{font-family:'Poppins',sans-serif;color:var(--ink);position:relative}
section,header,nav,footer{position:absolute;left:0;width:1200px}

/* top bar */
.topbar{top:0;height:85px;background:var(--blue)}
.topbar ul{list-style:none;display:flex;position:absolute;left:112px;top:0;height:85px;align-items:center;gap:0}
.topbar li{color:var(--white);font-size:15px;margin-right:60px}
.expert{position:absolute;right:0;top:0;width:344px;height:85px;background:var(--grey)}
.expert small{position:absolute;right:32px;top:20px;color:var(--white);font-size:12px;font-weight:500}
.expert .phone{position:absolute;left:57px;top:34px;display:flex;align-items:center;gap:12px;color:var(--white);font-family:'Oswald',sans-serif;font-size:22px}
.expert .phone span b{font-weight:500;font-size:24px}
.phone-badge{width:28px;height:26px;background:var(--white);border-radius:3px;display:flex;align-items:center;justify-content:center}

/* header */
.site-header{top:85px;height:104px}
.brand{position:absolute;left:112px;top:28px;display:flex;align-items:center;gap:12px}
.brand-mark{width:42px;height:42px;background:var(--green);border-radius:50%}
.brand-name{font-size:38px;font-weight:600;color:var(--blue)}
.search{position:absolute;left:788px;top:35px;width:300px;height:40px;background:var(--field);display:flex;align-items:center;padding:0 14px;font-size:11px;color:var(--grey-light);justify-content:space-between}

/* hero */
.hero{top:189px;height:594px;background:linear-gradient(135deg,#2b2c25 0%,#4a4a3c 35%,#3a3b30 60%,#1f211c 100%);text-align:center;color:var(--white)}
.hero-photo{position:absolute;inset:0;background:radial-gradient(ellipse at 52% 35%,rgba(140,110,80,.55),transparent 45%),radial-gradient(ellipse at 85% 70%,rgba(150,90,50,.45),transparent 35%)}
.hero h1{position:relative;margin-top:178px;font-size:46px;font-weight:500;line-height:63px;letter-spacing:.5px}
.hero p{position:relative;margin-top:17px;font-size:18px}
.btn{display:inline-block;background:var(--red);color:var(--white);font-size:16px;text-transform:uppercase;text-align:center}
.hero .btn{position:absolute;left:471px;top:367px;width:258px;height:68px;line-height:68px}

/* service tiles */
.services{top:783px;height:640px;background:var(--panel)}
.tile{position:absolute;width:308px;height:239px;background:var(--white);text-align:center}
.tile svg.icon{position:absolute;left:124px;top:38px}
.tile h2{position:absolute;width:100%;top:134px;font-size:19px;font-weight:400;color:var(--ink)}
.tile .arrow{position:absolute;left:24px;top:194px}
.tile.active{background:var(--blue)}
.tile.active h2{color:var(--white)}

/* news */
.news{top:1423px;height:395px}
.post{position:absolute;top:60px;width:308px}
.date{position:absolute;left:0;top:0;width:40px;height:46px;background:var(--grey);color:var(--white);text-align:center;font-size:17px;font-weight:600;line-height:22px;padding-top:2px}
.date small{display:block;font-size:12px;font-weight:400;line-height:14px}
.post h3{position:absolute;left:55px;top:2px;font-size:13px;font-weight:500;line-height:22px;text-transform:uppercase;color:var(--ink)}
.post .photo{position:absolute;left:0;top:60px;width:308px;height:119px}
.post p{position:absolute;left:0;top:128px;margin-top:0;top:250px}
.post .excerpt{position:absolute;top:190px;left:0;font-size:11.5px;line-height:21px;color:var(--muted)}

/* call to action */
.cta{top:1818px;height:334px;background:linear-gradient(90deg,#15263a 0%,#26403d 40%,#6f9a36 75%,#abd037 100%)}
.cta h2{position:absolute;left:112px;top:118px;font-family:'Oswald',sans-serif;font-weight:400;font-size:33px;line-height:49px;color:var(--white)}
.cta .btn{position:absolute;left:763px;top:136px;width:258px;height:67px;line-height:67px;font-size:17px}

/* social & signup */
.connect{top:2152px;height:223px;border-bottom:1px solid #e4e4e4}
.social{position:absolute;top:43px;left:0;width:100%;display:flex;justify-content:center;gap:34px}
.social span{width:53px;height:53px;border:2px solid var(--grey);border-radius:50%}
.signup{position:absolute;left:390px;top:128px;display:flex;gap:9px}
.signup .field{width:299px;height:42px;background:var(--field);font-size:11px;color:var(--grey);line-height:42px;padding-left:16px}
.signup .btn{width:112px;height:42px;line-height:42px;font-size:13px}

/* contact */
.contact{top:2375px;height:344px}
.contact h2{position:absolute;left:112px;top:37px;font-size:19px;font-weight:500}
.contact ul{list-style:none;position:absolute;left:112px;top:80px}
.contact li{display:flex;gap:10px;font-size:12px;line-height:22px;color:var(--ink);margin-bottom:14px}
.contact li svg{flex:none;margin-top:3px}
.hours{position:absolute;left:112px;top:214px;width:348px;height:34px;background:var(--field);display:flex;align-items:center;gap:18px;padding-left:12px;font-size:13px;font-weight:500}
.hours i{width:18px;height:18px;background:var(--grey);display:block}
.map{position:absolute;left:497px;top:41px;width:462px;height:214px;background:linear-gradient(160deg,#e6e3dc,#d9d6cd 60%,#cfd6c7)}
.copyright{position:absolute;left:0;width:100%;top:287px;text-align:center;font-size:11px;color:var(--muted)}
</style>
</head>
<body>

<nav class="topbar">
  <ul>
    <li>Home</li>
    <li>About Kelmora</li>
    <li>Ekhagen Hvb</li>
    <li>Work With Us</li>
    <li>Work With Us</li>
    <li>Plug</li>
  </ul>
  <div class="expert">
    <small>Speak With An Expert</small>
    <div class="phone">
      <div class="phone-badge"><svg width="16" height="16" viewBox="0 0 24 24"><path d="M6.6 10.8a15 15 0 006.6 6.6l2.2-2.2a1 1 0 011-.25 11.4 11.4 0 003.6.57 1 1 0 011 1V20a1 1 0 01-1 1A17 17 0 013 4a1 1 0 011-1h3.5a1 1 0 011 1c0 1.25.2 2.45.57 3.57a1 1 0 01-.25 1z" fill="#f04a50"/></svg></div>
      <span>CALL US: <b>010-4418260</b></span>
    </div>
  </div>
</nav>

<header class="site-header">
  <div class="brand"><span class="brand-mark"></span><span class="brand-name">Kelmora</span></div>
  <div class="search">Type Here
    <svg width="18" height="18" viewBox="0 0 24 24"><circle cx="10" cy="10" r="7" fill="none" stroke="#f04a50" stroke-width="2.4"/><line x1="15" y1="15" x2="21" y2="21" stroke="#f04a50" stroke-width="2.4"/></svg>
  </div>
</header>

<section class="hero">
  <div class="hero-photo" role="img" aria-label="Hands holding a small potted cactus in a garden"></div>
  <h1>Bedriva Vård, Omsorg Och Behandling<br>Av Högsta Kvalité.</h1>
  <p>Med Målet Att Ständigt Utvecklas, Förbättras Och Nå Bäst Resultat!</p>
  <span class="btn">Call Us Today</span>
</section>

<section class="services">
  <div class="tile active" style="left:112px;top:71px">
    <svg class="icon" width="60" height="80" viewBox="0 0 60 80" fill="none" stroke="#fff" stroke-width="2"><rect x="4" y="36" width="38" height="38"/><rect x="44" y="20" width="8" height="54"/><path d="M4 36l10-10h18l10 10"/><rect x="10" y="44" width="8" height="8"/><rect x="26" y="44" width="8" height="8"/><rect x="10" y="58" width="8" height="8"/><rect x="26" y="58" width="8" height="8"/></svg>
    <h2>HVB</h2>
    <svg class="arrow" width="34" height="14" viewBox="0 0 34 14"><path d="M0 7h32M26 1l6 6-6 6" fill="none" stroke="#fff" stroke-width="2"/></svg>
  </div>
  <div class="tile" style="left:446px;top:71px">
    <svg class="icon" width="60" height="80" viewBox="0 0 60 80" fill="none" stroke="#777" stroke-width="2"><rect x="4" y="36" width="38" height="38"/><rect x="44" y="20" width="8" height="54"/><path d="M4 36l10-10h18l10 10"/><rect x="10" y="44" width="8" height="8"/><rect x="26" y="44" width="8" height="8"/><rect x="10" y="58" width="8" height="8"/><rect x="26" y="58" width="8" height="8"/></svg>
    <h2>Stodboende</h2>
    <svg class="arrow" width="34" height="14" viewBox="0 0 34 14"><path d="M0 7h32M26 1l6 6-6 6" fill="none" stroke="#777" stroke-width="2"/></svg>
  </div>
  <div class="tile" style="left:780px;top:71px">
    <svg class="icon" width="60" height="80" viewBox="0 0 60 80" fill="none" stroke="#777" stroke-width="2"><path d="M8 18h44v56H8z"/><circle cx="8" cy="24" r="6"/><path d="M16 58l10-10 8 6 12-14M40 40h6v6"/></svg>
    <h2>Oppenvard</h2>
    <svg class="arrow" width="34" height="14" viewBox="0 0 34 14"><path d="M0 7h32M26 1l6 6-6 6" fill="none" stroke="#777" stroke-width="2"/></svg>
  </div>
  <div class="tile" style="left:112px;top:332px">
    <svg class="icon" width="60" height="80" viewBox="0 0 60 80" fill="none" stroke="#777" stroke-width="2"><circle cx="30" cy="44" r="26"/><circle cx="30" cy="44" r="12"/><path d="M30 18v14M56 44H42M30 70V56"/></svg>
    <h2>Vir behendsting</h2>
    <svg class="arrow" width="34" height="14" viewBox="0 0 34 14"><path d="M0 7h32M26 1l6 6-6 6" fill="none" stroke="#777" stroke-width="2"/></svg>
  </div>
  <div class="tile" style="left:446px;top:332px">
    <svg class="icon" width="60" height="80" viewBox="0 0 60 80" fill="none" stroke="#777" stroke-width="2"><circle cx="30" cy="34" r="13"/><path d="M8 76c0-16 10-24 22-24s22 8 22 24z"/></svg>
    <h2>Own Iss</h2>
    <svg class="arrow" width="34" height="14" viewBox="0 0 34 14"><path d="M0 7h32M26 1l6 6-6 6" fill="none" stroke="#777" stroke-width="2"/></svg>
  </div>
  <div class="tile" style="left:780px;top:332px">
    <svg class="icon" width="60" height="80" viewBox="0 0 60 80" fill="none" stroke="#777" stroke-width="2"><path d="M6 26h36v-8l14 14-14 14v-8H6z"/><path d="M20 50v16h-6l10 10 10-10h-6V50"/></svg>
    <h2>Piacering</h2>
    <svg class="arrow" width="34" height="14" viewBox="0 0 34 14"><path d="M0 7h32M26 1l6 6-6 6" fill="none" stroke="#777" stroke-width="2"/></svg>
  </div>
</section>

<section class="news">
  <article class="post" style="left:112px">
    <div class="date">02<small>May</small></div>
    <h3>Network Architecture/Design<br>And Engineering</h3>
    <div class="photo" role="img" aria-label="Go-kart parked in an indoor track" style="background:linear-gradient(120deg,#3a3a3c,#6c6c70 50%,#2a2a2c)"></div>
    <p class="excerpt">Sed diam nonummy nibh euismod tincidunt ut laoreet<br>dolore magna aliquam erat volutpat enim ad minim<br>veniam quis nostrud exerci tatullamco suscipit lobortis<br>nisl ut aliquip…</p>
  </article>
  <article class="post" style="left:446px">
    <div class="date">02<small>May</small></div>
    <h3>Network Architecture/Design<br>And Engineering</h3>
    <div class="photo" role="img" aria-label="Group of young people in winter jackets indoors" style="background:linear-gradient(120deg,#24262c,#5a5f6a 55%,#c9ccd2)"></div>
    <p class="excerpt">Sed diam nonummy nibh euismod tincidunt ut laoreet<br>dolore magna aliquam erat volutpat enim ad minim<br>veniam quis nostrud exerci tatullamco suscipit lobortis<br>nisl ut aliquip…</p>
  </article>
  <article class="post" style="left:780px">
    <div class="date">02<small>May</small></div>
    <h3>Network Architecture/Design<br>And Engineering</h3>
    <div class="photo" role="img" aria-label="Hands cutting food on a kitchen board" style="background:linear-gradient(120deg,#8a7f74,#b7aca0 50%,#5d544b)"></div>
    <p class="excerpt">Sed diam nonummy nibh euismod tincidunt ut laoreet<br>dolore magna aliquam erat volutpat enim ad minim<br>veniam quis nostrud exerci tatullamco suscipit lobortis<br>nisl ut aliquip…</p>
  </article>
</section>

<section class="cta" role="img" aria-label="House exterior under an evening sky with a blue to green overlay">
  <h2>Want to become a part of a business on the<br>move with the vision of being the best?</h2>
  <span class="btn">Work With Us !</span>
</section>

<section class="connect">
  <div class="social"><span></span><span></span><span></span></div>
  <div class="signup">
    <div class="field">Enter Your Mail Id:</div>
    <span class="btn">Sign Up</span>
  </div>
</section>

<footer class="contact">
  <h2>Contact Us</h2>
  <ul>
    <li><svg width="12" height="16" viewBox="0 0 12 16"><path d="M6 0a6 6 0 016 6c0 4.5-6 10-6 10S0 10.5 0 6a6 6 0 016-6z" fill="#3176b5"/><circle cx="6" cy="6" r="2.2" fill="#fff"/></svg><span>Kelmora Sverige AB Ekbacken 214<br>243 91 Höör</span></li>
    <li><svg width="14" height="14" viewBox="0 0 24 24"><path d="M6.6 10.8a15 15 0 006.6 6.6l2.2-2.2a1 1 0 011-.25 11.4 11.4 0 003.6.57 1 1 0 011 1V20a1 1 0 01-1 1A17 17 0 013 4a1 1 0 011-1h3.5a1 1 0 011 1c0 1.25.2 2.45.57 3.57a1 1 0 01-.25 1z" fill="#3176b5"/></svg><span style="font-size:14px">010-4418260</span></li>
    <li><svg width="14" height="11" viewBox="0 0 14 11"><rect width="14" height="11" fill="#3176b5"/><path d="M0 0l7 6 7-6" fill="none" stroke="#fff" stroke-width="1.4"/></svg><span style="font-size:11px;line-height:18px">info@kelmora.se<br>Org nr 559012-3345</span></li>
  </ul>
  <div class="hours"><i></i>Monday - Friday 09:00 - 18:00</div>
  <div class="map" role="img" aria-label="Street map showing the office location"></div>
  <p class="copyright">© All Rights Reserved. 2018</p>
</footer>

</body>
</html>
```